The Maple Sprout Clinic needs a Letterhead

We are a bilingual pediatric clinic located in Montreal, Canada.

Our english name is Maple Sprout Clinic
Our french name is Clinique du petit ruisseau

We offer complete care for children including general pediatric care, pediatric specialist care such as Ear, Nose and Throat, Urology, Neurology and Adolescent Medicine. We also have paramedical specialists such as psychologists, social workers, occupational therapists, speech and language pathologists.

The letterhead must use and be harmonious with our new logo. See Design #4923293. We need two types of letterhead. One for a the Logo and both english and french names on the top and the second with the list of current staff on the left. I have uploaded two old examples for you to see. Thanks and good luck.

Font styles to use
Sans Serif

Colors
3176b5
9d9d9d

Requirements
Must have
• Include our logo.
Nice to have
• Most of our printing is done in black and white. So a grayscale design is fine.
I have included a color and grayscale versions of our logo.

We prefer clean modern designs.

```html
<!DOCTYPE html>
<html lang="en">
<head>
<meta charset="utf-8">
<title>Maple Sprout Clinic – Letterhead</title>
<link rel="stylesheet" href="https://fonts.googleapis.com/css2?family=Didact+Gothic&display=swap">
<style>
  :root {
    --backdrop: #e9e9ea;
    --paper: #ffffff;
    --ink-grey: #8a8a8a;
    --band-grey: #6f6f6f;
    --mark-grey: #9d9d9d;
  }
  html, body {
    margin: 0;
    width: 1200px;
    height: 795px;
    overflow: hidden;
    background: var(--backdrop);
    font-family: "Didact Gothic", "Century Gothic", sans-serif;
  }
  .letterhead {
    position: absolute;
    left: 310px;
    top: 22px;
    width: 580px;
    height: 751px;
    background: var(--paper);
    box-shadow: 0 2px 10px rgba(0,0,0,0.12);
    overflow: hidden;
  }
  .brand {
    position: absolute;
    left: 34px;
    top: 36px;
    display: flex;
    align-items: center;
    gap: 8px;
    color: var(--ink-grey);
    font-size: 12px;
    line-height: 1.1;
  }
  .brand-name-fr { text-align: right; }
  .brand-name-en { text-align: left; }
  .brand-dot {
    width: 30px;
    height: 30px;
    border-radius: 50%;
    background: var(--ink-grey);
  }
  .corner-mark {
    position: absolute;
    right: 26px;
    bottom: 38px;
    width: 86px;
    height: 86px;
    border-radius: 50%;
    border: 12px solid var(--mark-grey);
    box-sizing: border-box;
  }
  .band-bottom {
    position: absolute;
    left: 0;
    right: 0;
    bottom: 0;
    height: 12px;
    background: var(--band-grey);
  }
  .band-side {
    position: absolute;
    right: 0;
    bottom: 0;
    width: 12px;
    height: 150px;
    background: var(--band-grey);
  }
  .contact {
    position: absolute;
    left: 34px;
    bottom: 22px;
    color: #555;
    font-size: 9.5px;
    line-height: 1.25;
  }
  .contact-line { display: flex; gap: 0; }
  .contact-phone { width: 232px; }
</style>
</head>
<body>
  <div class="letterhead">
    <header class="brand">
      <div class="brand-name-fr">Clinique<br>du petit<br>ruisseau</div>
      <div class="brand-dot" aria-hidden="true"></div>
      <div class="brand-name-en">Maple<br>Sprout<br>Clinic</div>
    </header>

    <div class="corner-mark" aria-hidden="true"></div>

    <footer class="contact">
      <div class="contact-line">2280 Rue des Érables, Suite 210, Lachine, QC H8T 2K5</div>
      <div class="contact-line">
        <span class="contact-phone">Phone: (514) 555 0187</span>
        <span class="contact-fax">Fax: (514) 555 0193</span>
      </div>
    </footer>

    <div class="band-side" aria-hidden="true"></div>
    <div class="band-bottom" aria-hidden="true"></div>
  </div>
</body>
</html>
```